Create a bold and border around my logo to make it pop and sign graphic design

I would like someone to create a sign graphic design so I can use on the side of my trucks and put on yard signs. I would to remove a lot of the white and add more of the orange and blue to give it more pop when cars drive past. I would like the services to be removed and for you to leave space for a mobile number that i would add later. I don’t want my logo changed at all. I just want colour and design to be added to the background so i can use it in signage. Same colour as on the sign

```html
<!DOCTYPE html>
<html lang="en">
<head>
<meta charset="utf-8">
<title>Branchworks – Vehicle &amp; Yard Sign</title>
<link rel="stylesheet" href="https://fonts.googleapis.com/css2?family=Lexend:wght@500;700&display=swap">
<style>
  :root {
    --brand-orange: #d4502a;
    --brand-blue: #233d80;
    --sign-white: #ffffff;
  }
  * { margin: 0; padding: 0; box-sizing: border-box; }
  html, body {
    width: 1200px;
    height: 599px;
    overflow: hidden;
    background: var(--brand-orange);
  }
  .sign {
    position: relative;
    width: 1200px;
    height: 599px;
    font-family: "Lexend", sans-serif;
  }
  .sign__upper {
    position: absolute;
    inset: 0 0 auto 0;
    height: 443px;
    background: var(--brand-orange);
  }
  .sign__lower {
    position: absolute;
    left: 0; right: 0; bottom: 0;
    height: 156px;
    background: var(--brand-blue);
  }
  .brand-mark {
    position: absolute;
    left: 492px;
    top: 72px;
    width: 216px;
    height: 216px;
  }
  .brand-plate {
    position: absolute;
    left: 192px;
    top: 292px;
    width: 828px;
    height: 108px;
    background: var(--sign-white);
    border-radius: 16px;
    display: flex;
    align-items: center;
    justify-content: center;
  }
  .brand-name {
    color: var(--brand-blue);
    font-weight: 700;
    font-size: 98px;
    line-height: 1;
    letter-spacing: 1px;
    padding-top: 6px;
  }
  .contact {
    position: absolute;
    left: 252px;
    top: 468px;
    height: 100px;
    display: flex;
    align-items: center;
    gap: 44px;
  }
  .contact__icon {
    width: 100px;
    height: 100px;
  }
  .contact__number {
    color: var(--sign-white);
    font-weight: 500;
    font-size: 82px;
    line-height: 1;
    letter-spacing: 1px;
  }
</style>
</head>
<body>
  <main class="sign">
    <div class="sign__upper"></div>
    <div class="sign__lower"></div>

    <svg class="brand-mark" viewBox="0 0 216 216" aria-hidden="true">
      <circle cx="108" cy="108" r="98" fill="none" stroke="var(--sign-white)" stroke-width="16"/>
    </svg>

    <div class="brand-plate">
      <span class="brand-name">BRANCHWORKS</span>
    </div>

    <div class="contact">
      <svg class="contact__icon" viewBox="0 0 100 100" aria-hidden="true">
        <circle cx="50" cy="50" r="43" fill="none" stroke="var(--sign-white)" stroke-width="7"/>
        <path fill="var(--sign-white)" d="M36 25c2-1 4 0 5 2l5 10c1 2 0 4-1 5l-4 3c2 6 7 11 13 14l3-4c1-1 3-2 5-1l10 5c2 1 3 3 2 5l-2 6c-1 3-4 5-8 4-17-3-31-17-34-34-1-4 1-7 4-8z"/>
      </svg>
      <span class="contact__number">(+91)-555-0142</span>
    </div>
  </main>
</body>
</html>
```